Business Card Design

Business card design.

Business card is to have logo, website address and email address.

Website is www.brightkettle.ie
Email is info@brightkettle.ie
Logo uploaded

I have ordered Business Card Printing via Print Harbor, the Double-sided colour printed option with gloss finish.

Industry/Entity Type

Business

```html
<!DOCTYPE html>
<html lang="en">
<head>
<meta charset="utf-8">
<title>Bright Kettle – Business Card</title>
<link rel="stylesheet" href="https://fonts.googleapis.com/css2?family=Archivo+Black&display=swap">
<style>
  :root {
    --stage: #8c1212;
    --card-white: #f7f7f7;
    --card-grey: #d9d9d9;
    --brand-red: #ee1c25;
    --brand-red-deep: #a3151b;
    --ink: #111111;
    --paper-text: #ffffff;
  }
  html, body {
    margin: 0;
    width: 1200px;
    height: 720px;
    overflow: hidden;
    background: var(--stage);
  }
  .canvas {
    position: relative;
    width: 1200px;
    height: 720px;
    font-family: "Archivo Black", "Arial Black", sans-serif;
  }
  .card {
    position: absolute;
    top: 210px;
    width: 520px;
    height: 300px;
    box-shadow: 0 6px 18px rgba(0, 0, 0, 0.45);
  }
  .card-contact { left: 60px; }
  .card-brand {
    left: 620px;
    background: linear-gradient(180deg, var(--card-white) 0%, var(--card-grey) 100%);
    display: flex;
    flex-direction: column;
    align-items: center;
    justify-content: center;
    gap: 22px;
  }
  .card-contact svg { display: block; }
  .contact-line {
    font-family: "Archivo Black", "Arial Black", sans-serif;
    font-size: 20px;
    fill: var(--paper-text);
    letter-spacing: 0.5px;
  }
  .brand-dot {
    width: 58px;
    height: 58px;
    border-radius: 50%;
    background: var(--brand-red);
  }
  .brand-name {
    margin: 0;
    font-size: 38px;
    font-weight: 400;
    color: var(--ink);
    letter-spacing: 0.5px;
  }
</style>
</head>
<body>
<main class="canvas">
  <section class="card card-contact" aria-label="Card back with contact details">
    <svg width="520" height="300" viewBox="0 0 520 300" xmlns="http://www.w3.org/2000/svg">
      <defs>
        <linearGradient id="redPanel" x1="0" y1="0" x2="0" y2="1">
          <stop offset="0" stop-color="#ee1c25"/>
          <stop offset="1" stop-color="#a3151b"/>
        </linearGradient>
      </defs>
      <rect class="card-base" width="520" height="300" fill="#f4f4f4"/>
      <rect class="red-panel" x="112" y="0" width="408" height="300" fill="url(#redPanel)"/>
      <rect class="rule" x="96" y="0" width="5" height="300" fill="#ee1c25"/>
      <rect class="rule-gap" x="101" y="0" width="7" height="300" fill="#f4f4f4"/>
      <circle class="emblem-ring" cx="110" cy="150" r="88" fill="#f4f4f4"/>
      <circle class="emblem-ring-line" cx="110" cy="150" r="80" fill="none" stroke="#ee1c25" stroke-width="4"/>
      <circle class="emblem" cx="110" cy="150" r="70" fill="#e01a22"/>
      <circle class="emblem-inner" cx="110" cy="150" r="60" fill="#c8161d"/>
      <text class="contact-line" x="245" y="130">www.brightkettle.ie</text>
      <text class="contact-line" x="245" y="180">info@brightkettle.ie</text>
    </svg>
  </section>

  <section class="card card-brand" aria-label="Card front with brand name">
    <div class="brand-dot"></div>
    <h1 class="brand-name">BRIGHTKETTLE.IE</h1>
  </section>
</main>
</body>
</html>
```